I'm looking for an app for customers to order through

I'm looking for an app for my customers to order products through
Ideally each customer would have a customer number with password
Their profile would come up with a preloaded products they currently order
From there they can select the product they require and volume needed for delivery
I would also like an option for them to go to a full product range if they are looking for Ideas or a product they don't currently use
Once the order is completed a copy of the order is them e-mailed to my distribution facilities and a confirmation sent to the customer by e-mail and/or SMS
Current product list is approx 1000 items
Current customers is 80 with expectations to expand to 200
On average current products ordered by each customer is is between 4-8 items
Ordering units are done by both weight and pieces/units

Target Market(s)

Food service outlets,
Restaurant , Hotels, catering companies, clubs, take away shops, cafes
Retail outlets

Number of Pages Required

1 page

Font styles to use
Sans Serif

Colors
abd037

Requirements
Must have
• Customer log in with Password 4 - 6 digit
• Customer order history
Nice to have
• Area for promotions / specials on a weekly / monthly basis

```html
<!DOCTYPE html>
<html lang="en">
<head>
<meta charset="utf-8">
<title>Harvest Supply – Ordering App Screens</title>
<link rel="stylesheet" href="https://fonts.googleapis.com/css2?family=Montserrat:wght@300;400;500&family=Source+Sans+3:wght@400&display=swap">
<style>
:root{
  --stage:#363636;
  --green:#7fa33a;
  --green-light:#abd037;
  --cream:#f1f1e6;
  --paper:#f4f4ec;
  --white:#ffffff;
  --text:#6b6b6b;
  --muted:#a6a6a6;
  --line:#d9d9cf;
  --red:#f26b6b;
  --price:#7a9a2e;
}
*{box-sizing:border-box;margin:0;padding:0}
html,body{width:1200px;height:800px;overflow:hidden;background:var(--stage)}
body{font-family:"Montserrat",sans-serif;position:relative}
.screen{position:absolute;top:64px;width:348px;height:618px;overflow:hidden;box-shadow:0 2px 8px rgba(0,0,0,.35)}
.screen--start{left:64px;background:var(--cream)}
.screen--products{left:426px;background:var(--paper)}
.screen--detail{left:788px;background:#efefef}
.status{position:absolute;left:0;top:0;width:100%;height:21px;font-size:10px;display:flex;align-items:center;padding:0 6px;color:#333}
.status--light{color:#fff}
.status .carrier{flex:1;display:flex;gap:6px;align-items:center}
.status .time{position:absolute;left:0;width:100%;text-align:center;pointer-events:none}
.status .battery{display:flex;align-items:center;gap:3px}
.status .battery i{display:inline-block;width:22px;height:8px;border:1px solid currentColor;border-radius:2px;background:currentColor}
.appbar{position:absolute;left:0;top:0;width:100%;background:var(--green);color:#fff}
.appbar .title{position:absolute;top:30px;left:0;width:100%;text-align:center;font-size:13px;font-weight:500}
.appbar svg{position:absolute}

/* start */
.brand{position:absolute;left:86px;top:82px;width:178px;height:70px;background:var(--green);display:flex;align-items:center;justify-content:center;gap:6px;color:#fff;box-shadow:0 1px 3px rgba(0,0,0,.25)}
.brand .dot{width:20px;height:20px;border-radius:50%;background:#fff}
.brand .name{font-size:12px;font-weight:500;line-height:1.1}
.welcome{position:absolute;top:184px;width:100%;text-align:center;color:var(--green);font-size:21px;font-weight:400}
.welcome b{font-weight:500}
.tagline{position:absolute;top:219px;width:100%;text-align:center;color:var(--muted);font-size:12.5px;font-weight:300}
.field{position:absolute;left:39px;width:270px;height:36px;border:1px solid var(--line);background:rgba(255,255,255,.35);display:flex;align-items:center;padding-left:12px;gap:10px;color:#bdbdb3;font-size:13px;font-weight:300}
.field .sep{width:1px;height:16px;background:var(--line)}
.btn-go{position:absolute;left:39px;top:384px;width:270px;height:36px;background:var(--green);color:#fff;font-size:13px;display:flex;align-items:center;justify-content:center}
.forgot{position:absolute;top:442px;width:100%;text-align:center;color:var(--muted);font-size:12px;font-weight:300}
.version{position:absolute;top:598px;width:100%;text-align:center;color:var(--muted);font-size:9px}

/* products */
.filters{position:absolute;top:57px;left:12px;display:flex;gap:3px}
.select{width:161px;height:21px;background:#fff;font-size:9px;color:#888;display:flex;align-items:center;justify-content:space-between;padding:0 7px}
.featured{position:absolute;top:98px;left:12px;width:324px;height:18px}
.featured::before{content:"";position:absolute;left:0;right:0;top:9px;height:1px;background:#e6dfb8}
.featured span{position:absolute;left:105px;width:114px;height:18px;border-radius:9px;background:#f7dfb5;color:#c8a878;font-size:9px;display:flex;align-items:center;justify-content:center}
.grid{position:absolute;top:131px;left:12px;display:grid;grid-template-columns:160px 160px;gap:6px 4px}
.card{height:154px;background:#fff;border:1px solid #ebebe3;position:relative}
.card .photo{position:absolute;left:14px;right:14px;top:8px;bottom:32px}
.card .meta{position:absolute;left:0;right:0;bottom:0;height:24px;background:#f2f2ee;display:flex;align-items:center;justify-content:space-between;padding:0 6px;font-size:10.5px;color:var(--text)}
.card .price{color:var(--price);font-size:10px}
.card .price small{font-size:7px}

.ph-dress{background:linear-gradient(#2ec8e0 0 45%,#9fe6ec 45% 65%,#cf3ba8 65%);border-radius:30% 30% 8px 8px}
.ph-suit{background:linear-gradient(#fafafa,#e6e6e6)}
.ph-jar{background:linear-gradient(#c65a1e,#7a2e10)}
.ph-cans{background:linear-gradient(90deg,#d94a40,#4fb06a,#d94a40)}
.ph-bags{background:linear-gradient(90deg,#e07a85,#dcd4c4,#5ab3a8)}
.ph-case{background:linear-gradient(160deg,#5a2e22 40%,#d92a2e 40%)}

/* detail */
.hero{position:absolute;top:53px;left:0;width:100%;height:337px;background:#fff}
.hero .photo{position:absolute;left:82px;top:15px;width:186px;height:280px;border-radius:30% 30% 10px 10px}
.hero .nav{position:absolute;top:150px;width:24px;height:24px;border-radius:50%;background:#eee;display:flex;align-items:center;justify-content:center}
.hero .dots{position:absolute;top:320px;width:100%;display:flex;justify-content:center;gap:3px}
.hero .dots i{width:4px;height:4px;border-radius:50%;background:#ddd}
.hero .dots i.on{background:var(--green)}
.summary{position:absolute;top:390px;left:0;width:100%;height:42px;background:#ececec;display:flex;align-items:center;justify-content:space-between;padding:0 12px;color:var(--text);font-size:13px;font-weight:400}
.summary .ship{display:flex;align-items:center;gap:4px;font-size:8px;color:#888;line-height:1.4}
.option{position:absolute;left:12px;width:324px;height:37px;background:#fff;display:flex;align-items:center;gap:14px;padding-left:10px;font-size:13px;color:var(--muted);font-weight:300}
.orderbar{position:absolute;left:0;top:576px;width:100%;height:42px;background:var(--green);display:flex;align-items:center;padding:0 0 0 12px;color:#fff;font-size:13px}
.qbtn{position:absolute;top:7px;width:27px;height:27px;display:flex;align-items:center;justify-content:center;font-size:14px}
.qbtn--minus{left:44px;background:var(--red)}
.qbtn--val{left:74px;border:1px solid #fff;background:#fff;color:#333;font-size:11px;outline:1px solid #6b8a2c}
.qbtn--plus{left:105px;background:var(--green-light)}
.total{position:absolute;right:74px;font-size:12px;font-weight:500}
.buy{position:absolute;left:281px;top:7px;width:55px;height:27px;background:var(--green-light);display:flex;align-items:center;justify-content:center;font-size:13px}

.caption{position:absolute;top:702px;width:348px;text-align:center;color:#fff;font-family:"Source Sans 3",sans-serif;font-size:24px}
</style>
</head>
<body>

<!-- Start screen -->
<section class="screen screen--start">
  <div class="status"><span class="carrier">●●●○○ Carrier</span><span class="time">4:21 PM</span><span class="battery">100% <i></i></span></div>
  <div class="brand"><span class="dot"></span><span class="name">HARVEST<br>SUPPLY</span></div>
  <h1 class="welcome">Welcome to <b>H.S.</b></h1>
  <p class="tagline">Lorem Ipsum is simply dummy text</p>
  <div class="field" style="top:276px">
    <svg width="14" height="14" viewBox="0 0 24 24"><path fill="#7fa33a" d="M6.6 10.8a15 15 0 0 0 6.6 6.6l2.2-2.2a1 1 0 0 1 1-.3 11 11 0 0 0 3.6.6 1 1 0 0 1 1 1V20a1 1 0 0 1-1 1A17 17 0 0 1 3 4a1 1 0 0 1 1-1h3.5a1 1 0 0 1 1 1c0 1.2.2 2.4.6 3.6a1 1 0 0 1-.3 1z"/></svg>
    <span class="sep"></span>Phone Number
  </div>
  <div class="field" style="top:320px">
    <svg width="14" height="14" viewBox="0 0 24 24"><rect x="4" y="10" width="16" height="12" fill="#7fa33a"/><path d="M8 10V7a4 4 0 0 1 8 0v3" fill="none" stroke="#7fa33a" stroke-width="2"/></svg>
    <span class="sep"></span>Password
  </div>
  <div class="btn-go">GO</div>
  <p class="forgot">Forget password?</p>
  <p class="version">v 1.0.1</p>
</section>

<!-- Product screen -->
<section class="screen screen--products">
  <header class="appbar" style="height:86px">
    <div class="status status--light"><span class="carrier">●●●○○ Carrier</span><span class="time">4:21 PM</span><span class="battery">100% <i></i></span></div>
    <svg style="left:12px;top:32px" width="18" height="14" viewBox="0 0 18 14"><path d="M0 1h18M0 7h18M0 13h18" stroke="#fff" stroke-width="1.6"/></svg>
    <div class="title">Products</div>
    <svg style="left:292px;top:31px" width="15" height="15" viewBox="0 0 16 16"><circle cx="6.5" cy="6.5" r="5" fill="none" stroke="#fff" stroke-width="1.4"/><path d="M10 10l5 5" stroke="#fff" stroke-width="1.6"/></svg>
    <svg style="left:319px;top:29px" width="17" height="16" viewBox="0 0 18 16"><path d="M1 7h16l-2 8H3z" fill="#fff"/><path d="M5 7l4-6M13 7l-2-4" stroke="#fff" stroke-width="1.4"/></svg>
    <div class="filters">
      <div class="select">All categories <svg width="9" height="6" viewBox="0 0 9 6"><path d="M1 1l3.5 3.5L8 1" fill="none" stroke="#888"/></svg></div>
      <div class="select">All services and shops <svg width="9" height="6" viewBox="0 0 9 6"><path d="M1 1l3.5 3.5L8 1" fill="none" stroke="#888"/></svg></div>
    </div>
  </header>
  <div class="featured"><span>Featured Items</span></div>
  <div class="grid">
    <article class="card"><div class="photo ph-dress" role="img" aria-label="Photo of a tiered child's dress"></div><div class="meta">Lorem Ipsum is <span class="price">40$<small>/pic</small></span></div></article>
    <article class="card"><div class="photo ph-suit" role="img" aria-label="Photo of a printed baby sleepsuit"></div><div class="meta">Lorem Ipsum is <span class="price">50$<small>/pic</small></span></div></article>
    <article class="card"><div class="photo ph-jar" role="img" aria-label="Photo of a jar of simmer sauce"></div><div class="meta">Lorem Ipsum is <span class="price">25$<small>/pic</small></span></div></article>
    <article class="card"><div class="photo ph-cans" role="img" aria-label="Photo of three food tins"></div><div class="meta">Lorem Ipsum is <span class="price">62$<small>/pic</small></span></div></article>
    <article class="card"><div class="photo ph-bags" role="img" aria-label="Photo of patterned lunch bags"></div><div class="meta">Lorem Ipsum is <span class="price">75$<small>/pic</small></span></div></article>
    <article class="card"><div class="photo ph-case" role="img" aria-label="Photo of leather pencil cases"></div><div class="meta">Lorem Ipsum is <span class="price">55$<small>/pic</small></span></div></article>
    <article class="card"></article>
    <article class="card"></article>
  </div>
</section>

<!-- Product detail screen -->
<section class="screen screen--detail">
  <header class="appbar" style="height:53px">
    <div class="status status--light"><span class="carrier">●●●○○ Carrier</span><span class="time">4:21 PM</span><span class="battery">100% <i></i></span></div>
    <svg style="left:14px;top:31px" width="9" height="14" viewBox="0 0 9 14"><path d="M8 1L2 7l6 6" fill="none" stroke="#fff" stroke-width="1.5"/></svg>
    <div class="title">Product Detail</div>
    <svg style="left:320px;top:29px" width="17" height="16" viewBox="0 0 18 16"><path d="M1 7h16l-2 8H3z" fill="#fff"/><path d="M5 7l4-6M13 7l-2-4" stroke="#fff" stroke-width="1.4"/></svg>
  </header>
  <div class="hero">
    <div class="photo ph-dress" role="img" aria-label="Large photo of a tiered child's dress"></div>
    <svg style="position:absolute;right:10px;top:6px" width="20" height="18" viewBox="0 0 24 22"><path d="M12 21L2 11a5.5 5.5 0 0 1 10-7 5.5 5.5 0 0 1 10 7z" fill="#e6e6e6"/></svg>
    <div class="nav" style="left:12px"><svg width="6" height="10" viewBox="0 0 6 10"><path d="M5 1L1 5l4 4" fill="none" stroke="#bbb"/></svg></div>
    <div class="nav" style="right:12px"><svg width="6" height="10" viewBox="0 0 6 10"><path d="M1 1l4 4-4 4" fill="none" stroke="#bbb"/></svg></div>
    <div class="dots"><i></i><i class="on"></i><i></i><i></i></div>
  </div>
  <div class="summary">Lorem Ipsum is simply dummy
    <span class="ship"><svg width="36" height="22" viewBox="0 0 36 22"><path d="M11 2h22v15H11zM11 7H5l-4 5v5h10" fill="none" stroke="#7fa33a" stroke-width="1.4"/><circle cx="7" cy="18" r="2.5" fill="#fff" stroke="#7fa33a" stroke-width="1.4"/><circle cx="27" cy="18" r="2.5" fill="#fff" stroke="#7fa33a" stroke-width="1.4"/><path d="M17 7h10l-2-2M27 12H17l2 2" fill="none" stroke="#7fa33a" stroke-width="1.2"/></svg>Lorem<br>Ipsum</span>
  </div>
  <div class="option" style="top:443px"><svg width="18" height="18" viewBox="0 0 18 18"><rect x="1" y="3" width="16" height="14" fill="none" stroke="#7fa33a" stroke-width="1.4"/><path d="M1 7h16M5 1v4M13 1v4M4 10h2M8 10h2M12 10h2M4 13h2M8 13h2M12 13h2" stroke="#7fa33a" stroke-width="1.4"/></svg>Delivery date &amp; time</div>
  <div class="option" style="top:484px"><svg width="18" height="18" viewBox="0 0 18 18"><path d="M9 17s-6-6-6-10a6 6 0 0 1 12 0c0 4-6 10-6 10z" fill="#7fa33a"/><circle cx="9" cy="7" r="2" fill="#fff"/></svg>Delivery address</div>
  <div class="option" style="top:525px"><svg width="18" height="14" viewBox="0 0 18 14"><rect x="1" y="1" width="16" height="12" fill="#7fa33a"/><path d="M1 1l8 7 8-7M1 13l6-6M17 13l-6-6" fill="none" stroke="#fff" stroke-width="1.2"/></svg>Card message</div>
  <div class="option" style="top:566px"></div>
  <div class="orderbar">Qty:
    <span class="qbtn qbtn--minus">−</span>
    <span class="qbtn qbtn--val">1</span>
    <span class="qbtn qbtn--plus">+</span>
    <span class="total">40.00$</span>
    <span class="buy">Buy</span>
  </div>
</section>

<p class="caption" style="left:64px">Start Screen</p>
<p class="caption" style="left:426px">Product Screen</p>
<p class="caption" style="left:788px">Product Detail Screen</p>

</body>
</html>
```